Need Bold, Hip Card for Concert Ticket Website Velvet Stubs!

Hi there! I am putting together a business/website that sells event tickets (mostly concerts, but also some sports and theater). Think PassDepot, but much smaller. The site is called Velvet Stubs. I have a new logo (attached, with black/red/white color scheme), and am looking for a modern/cool/original business card design. Note that I am thinking of having the card itself in the shape of a ticket (die cut), so you may want to keep that in mind when designing, but I'm not set on that. I'm also open to alternative card sizes, thicknesses, glossy, spot UV, etc. in order to stand out. I'm attaching a potential die cut template and a sample card using that template in case you want to work with that.
Target Market(s)
Music fans, people that like going to see live events
Industry/Entity Type
Entertainment
Contact Information for Business Card
Information that I'd like to have:
website address - www.velvetstubs-example.com
phone number: 1-833-5VELVETS (835-3887)
my name - Delia Hart
Look and feel
Each slider illustrates characteristics of the customer's brand and the style your logo design should communicate.

```html
<!DOCTYPE html>
<html lang="en">
<head>
<meta charset="utf-8">
<title>Velvet Stubs — Business Card</title>
<link rel="stylesheet" href="https://fonts.googleapis.com/css2?family=Montserrat:wght@800&family=Lato:wght@400;700&display=swap">
<style>
  :root {
    --page: #ecebe8;
    --card-white: #ffffff;
    --brand-red: #8b0000;
    --ink-black: #0a0a0a;
    --text-white: #ffffff;
    --card-w: 671px;
    --card-h: 414px;
  }
  * { box-sizing: border-box; margin: 0; padding: 0; }
  html, body {
    width: 1064px; height: 1200px; overflow: hidden;
    background: var(--page);
  }
  .card {
    position: absolute; left: 196px;
    width: var(--card-w); height: var(--card-h);
    overflow: hidden;
  }
  /* Front */
  .card--front { top: 168px; background: var(--card-white); }
  .front__brand {
    position: absolute; top: 0; left: 0; width: 100%; height: 212px;
    display: flex; align-items: center; justify-content: center; gap: 18px;
  }
  .brand__square { width: 64px; height: 64px; background: var(--brand-red); }
  .brand__name {
    font-family: "Montserrat", sans-serif; font-weight: 800;
    font-size: 50px; line-height: 1; color: var(--brand-red);
    letter-spacing: 2px; text-transform: uppercase;
  }
  .front__rule {
    position: absolute; top: 210px; left: 0; width: 100%; height: 3px;
    background: var(--ink-black);
  }
  .front__band {
    position: absolute; top: 217px; left: 0; width: 100%; bottom: 0;
    background: var(--brand-red);
    font-family: "Lato", sans-serif; color: var(--text-white);
  }
  .person { position: absolute; left: 95px; top: 64px; }
  .person__name { font-weight: 700; font-size: 27px; line-height: 1.1; text-transform: uppercase; }
  .person__role { font-weight: 400; font-size: 19px; margin-top: 2px; }
  .contacts { position: absolute; left: 344px; top: 48px; list-style: none; }
  .contacts li {
    display: flex; align-items: center; gap: 6px;
    font-size: 18px; line-height: 23px; white-space: nowrap;
  }
  .contacts svg { width: 16px; height: 16px; fill: var(--text-white); flex: none; }
  /* Back */
  .card--back { top: 631px; background: var(--ink-black); text-align: center; }
  .back__brand {
    position: absolute; top: 140px; left: 0; width: 100%;
    font-family: "Montserrat", sans-serif; font-weight: 800;
    font-size: 72px; line-height: 0.98; color: var(--text-white);
    letter-spacing: 6px; text-transform: uppercase;
  }
  .back__url {
    position: absolute; top: 326px; left: 0; width: 100%;
    font-family: "Lato", sans-serif; font-size: 19px;
    color: var(--text-white); letter-spacing: 1.5px;
  }
</style>
</head>
<body>
  <section class="card card--front">
    <div class="front__brand">
      <span class="brand__square"></span>
      <span class="brand__name">Velvet<br>Stubs</span>
    </div>
    <div class="front__rule"></div>
    <div class="front__band">
      <div class="person">
        <p class="person__name">Delia Hart</p>
        <p class="person__role">MANAGING DIRECTOR</p>
      </div>
      <ul class="contacts">
        <li><svg viewBox="0 0 16 16"><path d="M2 6c0-2 2-3 6-3s6 1 6 3v1h-3V6H5v1H2zM3 8h10l1 5H2z"/></svg>1-833-5VELVETS</li>
        <li><svg viewBox="0 0 16 16"><path d="M4 1h8v14H4zM5.5 3v9h5V3zM7 13h2v1H7z" fill-rule="evenodd"/></svg>(835-3887)</li>
        <li><svg viewBox="0 0 16 16"><path d="M1 3h14v10H1zM2.5 4.5 8 9l5.5-4.5z" fill-rule="evenodd"/></svg>info@velvetstubs-example.com</li>
        <li><svg viewBox="0 0 16 16"><circle cx="8" cy="8" r="7"/><path d="M4 5h3l1 3-2 1v3L4 9zM10 3l2 2-2 2z" fill="#8b0000"/></svg>www.velvetstubs-example.com</li>
      </ul>
    </div>
  </section>

  <section class="card card--back">
    <p class="back__brand">Velvet<br>Stubs</p>
    <p class="back__url">www.velvetstubs-example.com</p>
  </section>
</body>
</html>
```